Palvanor Lending. Website design for a mortgage company.

We need a simple, but classy and artistic website design. The website should contain a home page, about page, and information page. I would like the design for each page created and I can add the content.

Palvanor Lending is a retail mortgage broker business specially crafted to provide simple, transparent, and comprehensive mortgage solutions. We understand the complexities of mortgage acquisition and have aligned with the best partners and resources to analyze the information and deliver precise, transparent, efficient, and reliable results.

Target Market(s)

We are targeting people ages 30-65 within the United States, both male and female. We are also targeting business owners and property investors specifically.

Industry/Entity Type

Mortgage Brokerage

Coding

Coded - Design and coding required

Number of Pages Required

5+ page

Font styles to use
Sans Serif
Script

Requirements
Must have
• The main purpose of this website is to provide clients with the necessary information to want to move forward with a loan transaction. The website will be informational to promote the company and showcase our purpose. The company purpose is to provide efficient and comprehensive service to clients, and to help them navigate the challenging mortgage world.

The website must mimic that of the major fortune 500 companies. It needs to be super clean, but very modern. The pictures should be of families with brown skin mostly.

The website needs to be mobile responsive. Each page needs to consist of large and responsive Hero Images. There will be background videos on the product and process pages of the website.

The website must have a semi-flat design.
The website must have a Hamburger Menu instead of a visible navigation menu.

Use the script font styles for the headlines and the sans serif for body text.

We need to have the following pages:
Home

Products

Process

About

Contact - I want a map of our office location and region. We are located in Bowie MD and our region consists of the following states: Florida, Texas, Virginia, Maryland, and Washington DC.

```html
<!DOCTYPE html>
<html lang="en">
<head>
<meta charset="utf-8">
<title>Palvanor Lending — Website Design</title>
<link href="https://fonts.googleapis.com/css2?family=Lobster&family=Rubik:wght@400;500;700&family=Open+Sans:wght@400;600;700&display=swap" rel="stylesheet">
<style>
:root{
  --board-light:#e2e2e2;
  --board-dark:#3b3b3b;
  --white:#ffffff;
  --ink:#1d1d1d;
  --muted:#555a5e;
  --brand:#0d3b4a;
  --pink:#ff2d62;
  --sky:#eef9fd;
  --card:#1aa0d3;
  --rule:#e4e4e4;
}
*{margin:0;padding:0;box-sizing:border-box}
html,body{width:1200px;height:1200px;overflow:hidden}
body{position:relative;background:var(--board-light);font-family:"Open Sans",sans-serif;color:var(--ink)}
.board-dark{position:absolute;left:622px;top:0;width:578px;height:1200px;background:var(--board-dark)}
.screen{position:absolute;background:var(--white);overflow:hidden}
.abs{position:absolute}
.center{text-align:center}
.script{font-family:"Lobster",cursive;font-weight:400}
.brand-name{font-family:"Rubik",sans-serif;font-weight:700;color:var(--brand);letter-spacing:.2px;white-space:nowrap}
.brand-dot{position:absolute;border-radius:50%;background:var(--brand)}
.btn{position:absolute;background:var(--pink);color:#fff;border-radius:20px;font-family:"Rubik",sans-serif;display:flex;align-items:center;justify-content:center}
.photo{position:absolute}
.hero-photo{background:linear-gradient(120deg,#5b5550 0%,#47403b 35%,#5a5f58 60%,#3e3b38 100%)}
.hero-shade{position:absolute;inset:0;background:rgba(30,28,26,.35)}
.sunset-photo{background:linear-gradient(180deg,#ef7a45 0%,#f58a4e 40%,#e2552b 58%,#5c2a1d 75%,#3a1d16 100%)}
.coins-photo{background:linear-gradient(180deg,#95ad5c 0%,#b8c27a 18%,#8a7c62 45%,#b59a7a 70%,#d4c3ad 100%)}
.redwall-photo{background:linear-gradient(135deg,#b3432e 0%,#9b3526 55%,#3f4a44 100%)}
.yellow-photo{background:linear-gradient(180deg,#e9e1cf 0%,#ddd0b0 50%,#e6cf5a 80%,#d8bf45 100%)}
.hero-text{color:#fff}
.hero-label{position:absolute;color:#fff;font-family:"Rubik",sans-serif;font-weight:500;text-align:center;white-space:nowrap}
.nav a{position:absolute;font-size:5px;color:#333;text-decoration:none}
.title-script{position:absolute;left:0;right:0;text-align:center;color:var(--ink)}
.subtitle{position:absolute;left:0;right:0;text-align:center;font-family:"Rubik",sans-serif;color:var(--muted)}
.promise-item .num{position:absolute;border-radius:50%;border:1px solid #ececec;font-family:"Rubik",sans-serif;font-weight:700;display:flex;align-items:center;justify-content:center;box-shadow:0 1px 2px rgba(0,0,0,.08)}
.promise-item h4{position:absolute;font-weight:700;color:var(--ink)}
.promise-item p{position:absolute;color:var(--muted)}
.rule{position:absolute;height:1px;background:var(--rule)}
.card{position:absolute;background:linear-gradient(180deg,var(--card) 0%,var(--card) 55%,rgba(26,160,211,.55) 82%,rgba(26,160,211,0) 100%);color:#fff;text-align:center}
.card h5{position:absolute;left:4px;right:4px;font-weight:700}
.card p{position:absolute;left:8px;right:8px}
.testimonial h6{font-family:"Rubik",sans-serif;font-weight:700;color:#444;text-transform:uppercase;letter-spacing:.2px}
.testimonial p{color:#444}
.footer{position:absolute;left:0;right:0;background:var(--brand);color:#fff;text-align:center}
.footer .links{position:absolute;left:0;right:0;font-family:"Rubik",sans-serif;font-weight:500}
.footer .links span{margin:0 6px}
.social{position:absolute;left:0;right:0;display:flex;justify-content:center}
.social i{display:block;border-radius:50%;background:#9fb6bf}
.footer .copy{position:absolute;left:0;right:0}
</style>
</head>
<body>
<div class="board-dark"></div>

<!-- ================= DESKTOP ================= -->
<section class="screen desktop" style="left:75px;top:70px;width:463px;height:1059px">
  <header class="abs" style="left:0;top:0;width:463px;height:24px;background:#fff">
    <span class="brand-dot" style="left:28px;top:6px;width:12px;height:12px"></span>
    <span class="abs brand-name" style="left:47px;top:7px;font-size:7.5px">PALVANOR LENDING</span>
    <nav class="nav">
      <a style="left:242px;top:10px">Home</a>
      <a style="left:272px;top:10px">Products</a>
      <a style="left:309px;top:10px">Process</a>
      <a style="left:344px;top:10px">About</a>
      <a style="left:375px;top:10px">Contact</a>
    </nav>
    <svg class="abs" style="left:413px;top:8px" width="9" height="7" viewBox="0 0 9 7"><path d="M0 .5h9M0 3.5h9M0 6.5h9" stroke="#999" stroke-width=".8"/></svg>
  </header>

  <div class="photo hero-photo" role="img" aria-label="Parent and daughter washing hands at a kitchen sink" style="left:0;top:24px;width:463px;height:239px"><div class="hero-shade"></div></div>
  <div class="abs hero-text center" style="left:0;top:24px;width:463px;height:239px">
    <h1 class="script abs" style="left:0;right:0;top:20px;font-size:22px">Quick and Easy.</h1>
    <p class="abs" style="left:130px;right:130px;top:53px;font-size:5px;line-height:8px">Palvanor Lending is a retail mortgage broker business specially crafted to provide simple, transparent, and comprehensive mortgage solutions.<br>See what we provide.</p>
    <div class="btn" style="left:200px;top:92px;width:63px;height:16px;font-size:5.5px">Get started</div>

    <svg class="abs" style="left:88px;top:136px" width="28" height="28" viewBox="0 0 48 48" fill="none" stroke="#fff" stroke-width="2.5" stroke-linejoin="round"><path d="M4 22 24 6l20 16M9 18v24h10V30h10v12h10V18"/></svg>
    <svg class="abs" style="left:172px;top:136px" width="32" height="28" viewBox="0 0 52 44" fill="none" stroke="#fff" stroke-width="2.5"><circle cx="5" cy="6" r="3.5"/><circle cx="5" cy="22" r="3.5"/><circle cx="5" cy="38" r="3.5"/><path d="M14 6h36M14 22h36M14 38h36"/></svg>
    <svg class="abs" style="left:259px;top:137px" width="31" height="26" viewBox="0 0 52 44" fill="none" stroke="#fff" stroke-width="2.3"><rect x="2" y="14" width="38" height="26" rx="2"/><path d="M7 14V9h38v26h-5M12 9V4h38v26h-5"/><circle cx="21" cy="27" r="7"/><path d="M23.5 23.5h-4a2 2 0 0 0 0 4h3a2 2 0 0 1 0 4h-4M21 21.5v12"/></svg>
    <svg class="abs" style="left:347px;top:132px" width="32" height="32" viewBox="0 0 48 48" fill="none" stroke="#fff" stroke-width="2.3" stroke-linejoin="round"><rect x="4" y="2" width="20" height="40" rx="3"/><path d="M11 6h6M12 28V14a3 3 0 0 1 6 0v10l10 2c4 1 6 3 5 7l-2 9H18l-8-10c-2-3 1-5 3-3l5 4"/><path d="M8 12l3 2M7 18h4M9 7l2 3"/></svg>

    <span class="hero-label" style="left:70px;width:64px;top:167px;font-size:7px">Home Purchase</span>
    <span class="hero-label" style="left:148px;width:80px;top:167px;font-size:7px">Mortgage Checklist</span>
    <span class="hero-label" style="left:240px;width:68px;top:167px;font-size:7px">Credit Tips</span>
    <span class="hero-label" style="left:325px;width:74px;top:167px;font-size:7px">Loan Selection</span>

    <svg class="abs" style="left:226px;top:203px" width="10" height="12" viewBox="0 0 10 12" fill="none" stroke="#ddd" stroke-width=".8"><path d="M5 0v11M1 7l4 4 4-4"/></svg>
  </div>

  <section class="why">
    <h2 class="title-script script" style="top:302px;font-size:14px">Why Choose Us</h2>
    <p class="subtitle" style="top:328px;font-size:6.5px">The Palvanor Lending Promise</p>
    <div class="rule" style="left:53px;top:357px;width:182px"></div>
    <div class="promise-item">
      <div class="num" style="left:68px;top:367px;width:18px;height:18px;font-size:8px">1</div>
      <h4 style="left:91px;top:364px;font-size:5px">Best Loan. Most Savings.</h4>
      <p style="left:91px;top:372px;width:140px;font-size:4.6px;line-height:7.5px">Our Digital Loan Officer analyzes thousands of options to show you the loan that saves you the most money possible.</p>
    </div>
    <div class="rule" style="left:53px;top:404px;width:182px"></div>
    <div class="promise-item">
      <div class="num" style="left:68px;top:413px;width:18px;height:18px;font-size:8px">2</div>
      <h4 style="left:91px;top:411px;font-size:5px">Our Mortgage is so simple.</h4>
      <p style="left:91px;top:419px;width:140px;font-size:4.6px;line-height:7.5px">Whether you are here to buy or refinance it only takes 10-15 minutes to fill out our simple application.</p>
    </div>
    <div class="rule" style="left:53px;top:443px;width:182px"></div>
    <div class="promise-item">
      <div class="num" style="left:68px;top:452px;width:18px;height:18px;font-size:8px">3</div>
      <h4 style="left:91px;top:450px;font-size:5px">Trusted. Local. Experts.</h4>
      <p style="left:91px;top:458px;width:140px;font-size:4.6px;line-height:7.5px">We're around the corner and ready to help you. our goal is to ensure every customer is so happy, they gladly refer us to family and friends.</p>
    </div>
    <div class="rule" style="left:53px;top:489px;width:182px"></div>
    <div class="photo sunset-photo" role="img" aria-label="Family walking together on a beach at sunset" style="left:245px;top:369px;width:164px;height:110px"></div>
  </section>

  <section class="abs" style="left:0;top:519px;width:463px;height:74px;background:var(--sky)">
    <h2 class="title-script script" style="top:18px;font-size:14px">Start Saving Now</h2>
    <p class="subtitle" style="top:44px;font-size:6.5px">Don't Pay For Your Mistake With Every Payment You Make.</p>
  </section>

  <div class="photo coins-photo" role="img" aria-label="Stacks of coins beside a small wooden house model" style="left:0;top:593px;width:463px;height:214px"></div>

  <article class="card" style="left:58px;top:622px;width:109px;height:140px">
    <svg class="abs" style="left:39px;top:10px" width="32" height="32" viewBox="0 0 48 48" fill="none" stroke="#fff" stroke-width="3" stroke-linejoin="round"><path d="M34 20V4H6v40h28v-6M12 12h16M12 20h14M12 28h10M12 36h8"/><path d="M40 16l5 5-17 17-7 2 2-7z"/></svg>
    <h5 style="top:53px;font-size:5px">Start your Pre-Approval Today</h5>
    <p style="top:70px;font-size:4.6px;line-height:7.8px">To become pre-approved for a home loan, please fill out our online application and your Loan Officer will contact you immediately to discuss the details.</p>
    <div class="btn" style="left:31px;top:120px;width:46px;height:15px;font-size:5px">More</div>
  </article>
  <article class="card" style="left:176px;top:622px;width:109px;height:140px">
    <svg class="abs" style="left:39px;top:12px" width="31" height="28" viewBox="0 0 48 44" fill="none" stroke="#fff" stroke-width="3.4" stroke-linejoin="round"><path d="M3 20 24 3l21 17M9 16v25h30V16"/><rect x="17" y="24" width="6" height="6"/><rect x="25" y="24" width="6" height="6"/><path d="M20 41V33h8v8"/></svg>
    <h5 style="top:53px;font-size:5px">I'm buying/refinancing home</h5>
    <p style="top:70px;font-size:4.6px;line-height:7.8px">Buying or refinancing a home takes time, patience, and, traditionally, a lot of paperwork. We've dismantled the old mortgage infrastructure and replaced it.</p>
    <div class="btn" style="left:31px;top:120px;width:46px;height:15px;font-size:5px">More</div>
  </article>
  <article class="card" style="left:295px;top:622px;width:109px;height:134px">
    <svg class="abs" style="left:38px;top:10px" width="33" height="33" viewBox="0 0 48 48" fill="none" stroke="#fff" stroke-width="3.4"><circle cx="24" cy="24" r="21"/><path d="M31 16h-9a5 5 0 0 0 0 10h4a5 5 0 0 1 0 10h-10M24 10v28"/></svg>
    <h5 style="top:53px;font-size:4.8px;line-height:5.5px">Other loans<br>(FHA, USDA, Jumb, VA)</h5>
    <p style="top:74px;font-size:4.6px;line-height:7.8px">Palvanor Lending offers traditional and tailored loan options. Our competitive loan options can help meet your needs.</p>
    <div class="btn" style="left:31px;top:116px;width:46px;height:15px;font-size:5px">More</div>
  </article>

  <section class="testimonial">
    <div class="abs" style="left:100px;width:155px;top:829px;text-align:right">
      <h6 style="font-size:4.8px">Our Customer Testimonials</h6>
      <p style="font-size:4.6px;line-height:8px">"I refinanced my home with Palvanor Lending. They answered all our questions, was always prompt in their responses and made the experience easy. They helped me get a great rate, and I couldn't have done it without them."<br>- Darnell on May 5, 2020</p>
    </div>
    <div class="photo redwall-photo" role="img" aria-label="Father playing with his toddler in front of a red wall" style="left:275px;top:827px;width:70px;height:76px"></div>
  </section>
  <section class="testimonial">
    <div class="photo yellow-photo" role="img" aria-label="Mother and daughter in matching yellow dresses" style="left:117px;top:941px;width:70px;height:46px"></div>
    <div class="abs" style="left:208px;width:135px;top:944px">
      <h6 style="font-size:4.8px">Our Customer Testimonials</h6>
      <p style="font-size:4.6px;line-height:8px">"They are very professional and quick in contact us for any loan updates. They closed my loan in a short period of time. " - Keisha on May 20, 2020</p>
    </div>
  </section>

  <footer class="footer" style="top:1007px;height:52px">
    <div class="links" style="top:11px;font-size:5px"><span>About us</span><span>Services</span><span>Get In Touch</span><span>Process</span><span>Policy</span></div>
    <div class="social" style="top:23px;gap:6px"><i style="width:6px;height:6px"></i><i style="width:6px;height:6px"></i><i style="width:6px;height:6px"></i><i style="width:6px;height:6px"></i><i style="width:6px;height:6px"></i><i style="width:6px;height:6px"></i></div>
    <p class="copy" style="top:35px;font-size:4.8px">© Copyright 2020 Palvanor Lending - All Rights Reserved</p>
  </footer>
</section>

<!-- ================= MOBILE 1 ================= -->
<section class="screen mobile-home" style="left:727px;top:42px;width:185px;height:1091px">
  <header class="abs" style="left:0;top:0;width:185px;height:34px;background:#fff">
    <span class="brand-dot" style="left:9px;top:6px;width:18px;height:18px"></span>
    <span class="abs brand-name" style="left:38px;top:11px;font-size:8.8px">PALVANOR LENDING</span>
  </header>
  <div class="photo hero-photo" role="img" aria-label="Parent and daughter washing hands at a kitchen sink" style="left:0;top:34px;width:185px;height:554px"><div class="hero-shade"></div></div>
  <div class="abs hero-text center" style="left:0;top:34px;width:185px;height:554px">
    <h1 class="script abs" style="left:0;right:0;top:40px;font-size:18.5px">Quick and Easy.</h1>
    <p class="abs" style="left:14px;right:14px;top:75px;font-size:7.3px;line-height:11.2px">Palvanor Lending is a retail mortgage broker business specially crafted to provide simple, transparent, and comprehensive mortgage solutions.<br>See what we provide.</p>
    <div class="btn" style="left:53px;top:152px;width:78px;height:25px;font-size:5.8px">Get started</div>

    <svg class="abs" style="left:71px;top:214px" width="43" height="41" viewBox="0 0 48 46" fill="none" stroke="#fff" stroke-width="2.6" stroke-linejoin="round"><path d="M3 22 24 4l21 18M9 17v27h10V31h10v13h10V17"/></svg>
    <span class="hero-label" style="left:0;right:0;top:264px;font-size:9px">Home Purchase</span>
    <svg class="abs" style="left:70px;top:290px" width="43" height="36" viewBox="0 0 52 44" fill="none" stroke="#fff" stroke-width="2.5"><circle cx="5" cy="6" r="3.8"/><circle cx="5" cy="22" r="3.8"/><circle cx="5" cy="38" r="3.8"/><path d="M14 6h36M14 22h36M14 38h36"/></svg>
    <span class="hero-label" style="left:0;right:0;top:341px;font-size:9px">Mortgage Checklist</span>
    <svg class="abs" style="left:71px;top:384px" width="44" height="36" viewBox="0 0 52 44" fill="none" stroke="#fff" stroke-width="2.3"><rect x="2" y="14" width="38" height="26" rx="2"/><path d="M7 14V9h38v26h-5M12 9V4h38v26h-5"/><circle cx="21" cy="27" r="7"/><path d="M23.5 23.5h-4a2 2 0 0 0 0 4h3a2 2 0 0 1 0 4h-4M21 21.5v12"/></svg>
    <span class="hero-label" style="left:0;right:0;top:429px;font-size:9px">Credit Tips</span>
    <svg class="abs" style="left:70px;top:455px" width="44" height="44" viewBox="0 0 48 48" fill="none" stroke="#fff" stroke-width="2.3" stroke-linejoin="round"><rect x="4" y="2" width="20" height="40" rx="3"/><path d="M11 6h6M12 28V14a3 3 0 0 1 6 0v10l10 2c4 1 6 3 5 7l-2 9H18l-8-10c-2-3 1-5 3-3l5 4"/><path d="M8 12l3 2M7 18h4M9 7l2 3"/></svg>
    <span class="hero-label" style="left:0;right:0;top:506px;font-size:9px">Loan Selection</span>
  </div>

  <section class="why">
    <h2 class="title-script script" style="top:643px;font-size:13.5px">Why Choose Us</h2>
    <p class="subtitle" style="top:673px;font-size:8.5px">The Palvanor Lending Promise</p>
    <div class="photo sunset-photo" role="img" aria-label="Family walking together on a beach at sunset" style="left:7px;top:711px;width:171px;height:114px"></div>
    <div class="promise-item">
      <div class="num" style="left:25px;top:850px;width:20px;height:20px;font-size:9px">1</div>
      <h4 style="left:50px;width:120px;top:848px;font-size:7.3px;text-align:center">Best Loan. Most Savings.</h4>
      <p style="left:50px;width:120px;top:859px;font-size:7.3px;line-height:11px;text-align:center">Our Digital Loan Officer analyzes thousands of options to show you the loan that saves you the most money possible.</p>
    </div>
    <div class="rule" style="left:7px;top:913px;width:171px"></div>
    <div class="promise-item">
      <div class="num" style="left:25px;top:926px;width:20px;height:20px;font-size:9px">2</div>
      <h4 style="left:50px;width:120px;top:924px;font-size:7.3px;text-align:center">Our Mortgage is so simple.</h4>
      <p style="left:50px;width:120px;top:935px;font-size:7.3px;line-height:11px;text-align:center">Whether you are here to buy or refinance it only takes 10-15 minutes to fill out our simple application.</p>
    </div>
    <div class="rule" style="left:7px;top:989px;width:171px"></div>
    <div class="promise-item">
      <div class="num" style="left:25px;top:1002px;width:20px;height:20px;font-size:9px">3</div>
      <h4 style="left:50px;width:120px;top:1000px;font-size:7.3px;text-align:center">Trusted. Local. Experts.</h4>
      <p style="left:50px;width:120px;top:1011px;font-size:7.3px;line-height:11px;text-align:center">We're around the corner and ready to help you. our goal is to ensure every customer is so happy, they gladly refer us to family and friends.</p>
    </div>
    <div class="rule" style="left:7px;top:1076px;width:171px"></div>
  </section>
</section>

<!-- ================= MOBILE 2 ================= -->
<section class="screen mobile-saving" style="left:953px;top:42px;width:142px;height:1146px">
  <section class="abs" style="left:0;top:0;width:142px;height:86px;background:var(--sky)">
    <h2 class="title-script script" style="top:22px;font-size:10.5px">Start Saving Now</h2>
    <p class="subtitle" style="top:44px;left:8px;right:8px;font-size:6px;line-height:9px">Don't Pay For Your Mistake With Every Payment You Make.</p>
  </section>
  <div class="photo coins-photo" role="img" aria-label="Stacks of coins beside a small wooden house model" style="left:0;top:86px;width:142px;height:565px"></div>

  <article class="card" style="left:10px;top:117px;width:121px;height:160px">
    <svg class="abs" style="left:44px;top:11px" width="34" height="34" viewBox="0 0 48 48" fill="none" stroke="#fff" stroke-width="3" stroke-linejoin="round"><path d="M34 20V4H6v40h28v-6M12 12h16M12 20h14M12 28h10M12 36h8"/><path d="M40 16l5 5-17 17-7 2 2-7z"/></svg>
    <h5 style="top:57px;font-size:5px">Start your Pre-Approval Today</h5>
    <p style="top:74px;font-size:5px;line-height:8.6px">To become pre-approved for a home loan, please fill out our online application and your Loan Officer will contact you immediately to discuss the details.</p>
    <div class="btn" style="left:38px;top:127px;width:46px;height:19px;font-size:4.5px">More</div>
  </article>
  <article class="card" style="left:10px;top:286px;width:121px;height:160px">
    <svg class="abs" style="left:44px;top:13px" width="33" height="30" viewBox="0 0 48 44" fill="none" stroke="#fff" stroke-width="3.4" stroke-linejoin="round"><path d="M3 20 24 3l21 17M9 16v25h30V16"/><rect x="17" y="24" width="6" height="6"/><rect x="25" y="24" width="6" height="6"/><path d="M20 41V33h8v8"/></svg>
    <h5 style="top:57px;font-size:5px">I'm buying/refinancing home</h5>
    <p style="top:74px;font-size:5px;line-height:8.6px">Buying or refinancing a home takes time, patience, and, traditionally, a lot of paperwork. We've dismantled the old mortgage infrastructure and replaced it.</p>
    <div class="btn" style="left:38px;top:127px;width:46px;height:19px;font-size:4.5px">More</div>
  </article>
  <article class="card" style="left:10px;top:455px;width:121px;height:160px">
    <svg class="abs" style="left:43px;top:11px" width="35" height="35" viewBox="0 0 48 48" fill="none" stroke="#fff" stroke-width="3.4"><circle cx="24" cy="24" r="21"/><path d="M31 16h-9a5 5 0 0 0 0 10h4a5 5 0 0 1 0 10h-10M24 10v28"/></svg>
    <h5 style="top:56px;font-size:5px;line-height:5.6px">Other loans<br>(FHA, USDA, Jumb, VA)</h5>
    <p style="top:79px;font-size:5px;line-height:8.6px">Palvanor Lending offers traditional and tailored loan options. Our competitive loan options can help meet your needs.</p>
    <div class="btn" style="left:38px;top:125px;width:46px;height:19px;font-size:4.5px">More</div>
  </article>

  <section class="testimonial abs center" style="left:6px;right:6px;top:672px">
    <h6 style="font-size:5px">Our Customer Testimonials</h6>
    <p style="font-size:5px;line-height:8.6px">"I refinanced my home with Palvanor Lending. They answered all our questions, was always prompt in their responses and made the experience easy. They helped me get a great rate, and I couldn't have done it without them."<br>- Darnell on May 5, 2020</p>
  </section>
  <div class="photo redwall-photo" role="img" aria-label="Father playing with his toddler in front of a red wall" style="left:8px;top:747px;width:121px;height:132px"></div>
  <div class="photo yellow-photo" role="img" aria-label="Mother and daughter in matching yellow dresses" style="left:8px;top:920px;width:121px;height:81px"></div>
  <section class="testimonial abs" style="left:8px;right:6px;top:1007px">
    <h6 style="font-size:5px">Our Customer Testimonials</h6>
    <p style="font-size:5px;line-height:8.4px">"They are very professional and quick in contact us for any loan updates. They closed my loan in a short period of time. " - Keisha on May 20, 2020</p>
  </section>

  <footer class="footer" style="top:1070px;height:76px">
    <div class="links" style="top:10px;font-size:5.2px"><span>About us</span><span>Services</span><span>Get In Touch</span></div>
    <div class="links" style="top:24px;font-size:5.2px"><span>Process</span><span>Policy</span></div>
    <div class="social" style="top:38px;gap:6px"><i style="width:6px;height:6px"></i><i style="width:6px;height:6px"></i><i style="width:6px;height:6px"></i><i style="width:6px;height:6px"></i><i style="width:6px;height:6px"></i><i style="width:6px;height:6px"></i></div>
    <p class="copy" style="top:50px;left:8px;right:8px;font-size:5.2px;line-height:8.5px">© Copyright 2020 Palvanor Lending - All Rights Reserved</p>
  </footer>
</section>
</body>
</html>
```